Business Card Design

We require a business card design for a law firm, our signature colours are maroon and cream. Our slogan is "From our family to yours", we would like the cards to be professional however feminine at the same time.

Industry/Entity Type

Business

Contact Information for Business Card

Helena Brackett & Associates Lawyers & Conveyancers, Helena Brackett LL.B. Principal Solicitor, 17 Quillon Street, Marrowdale NSW 2190

Logo styles of interest
Emblem Logo
Abstract Logo
Wordmark Logo

```html
<!DOCTYPE html>
<html lang="en">
<head>
<meta charset="utf-8">
<title>Helena Brackett &amp; Associates — Business Card</title>
<link rel="stylesheet" href="https://fonts.googleapis.com/css2?family=Courier+Prime&family=Source+Sans+3:wght@300;400;700&display=swap">
<style>
  :root {
    --cream-light: #fbf7ee;
    --cream-edge: #ece2cc;
    --ink: #1d1916;
    --ink-soft: #2b2521;
    --rule: #5e4f45;
    --taupe: #a88c7b;
    --taupe-pale: #cdb8a8;
  }
  html, body {
    margin: 0;
    padding: 0;
    width: 1200px;
    height: 742px;
    overflow: hidden;
    background: var(--cream-edge);
  }
  .card {
    position: relative;
    width: 1200px;
    height: 742px;
    overflow: hidden;
    background: radial-gradient(ellipse at 45% 40%, var(--cream-light) 0%, #f6efe0 45%, var(--cream-edge) 100%);
  }
  .emblem {
    position: absolute;
    left: 180px;
    top: 90px;
    width: 300px;
    height: 300px;
  }
  .firm {
    position: absolute;
    left: 40px;
    top: 440px;
    width: 540px;
    text-align: center;
    color: var(--ink);
    font-family: "Source Sans 3", "Helvetica Neue", Arial, sans-serif;
  }
  .firm-name {
    margin: 0;
    font-weight: 700;
    font-size: 58px;
    line-height: 64px;
    letter-spacing: -0.5px;
  }
  .firm-tagline {
    margin: 6px 0 0;
    font-weight: 400;
    font-size: 36px;
    line-height: 44px;
  }
  .divider {
    position: absolute;
    left: 598px;
    top: 69px;
    width: 3px;
    height: 601px;
    background: var(--rule);
  }
  .contact {
    position: absolute;
    left: 640px;
    top: 130px;
    width: 520px;
    margin: 0;
    text-align: center;
    color: var(--ink-soft);
    font-family: "Courier Prime", "Courier New", monospace;
    font-size: 36px;
    line-height: 54px;
    word-spacing: 6px;
    font-style: normal;
  }
  .contact span { display: block; }
  .flourish {
    position: absolute;
    left: 670px;
    top: 355px;
    width: 455px;
    height: 235px;
  }
</style>
</head>
<body>
  <main class="card">
    <svg class="emblem" viewBox="0 0 300 300" role="img" aria-label="Firm emblem">
      <circle cx="150" cy="150" r="140" fill="var(--taupe)" opacity="0.28"/>
    </svg>

    <div class="firm">
      <p class="firm-name">Helena Brackett<br>&amp; Associates</p>
      <p class="firm-tagline">Lawyers &amp; Conveyancers</p>
    </div>

    <div class="divider"></div>

    <address class="contact">
      <span>Helena Brackett</span>
      <span>LL.B. Principal Solicitor</span>
      <span>17 Quillon Street</span>
      <span>Marrowdale NSW 2190</span>
    </address>

    <svg class="flourish" viewBox="0 0 455 235" role="img" aria-label="Decorative heart-shaped flourish ornament">
      <defs>
        <radialGradient id="flourishTone" cx="50%" cy="45%" r="60%">
          <stop offset="0%" stop-color="var(--taupe-pale)" stop-opacity="0.55"/>
          <stop offset="100%" stop-color="var(--taupe-pale)" stop-opacity="0"/>
        </radialGradient>
      </defs>
      <rect x="0" y="0" width="455" height="235" rx="110" fill="url(#flourishTone)"/>
    </svg>
  </main>
</body>
</html>
```